Real Estate Webpage Design

We have an existing website: brindlewoodhomes.com.au
We focus customised service mainly on Property Management and second-hand property sales.
We are not entirely happy about the current design and layout can stay roughly the same as the back end coding is linked to a CRM system.
We would like to see the design are more reachable to our clients and appearing.
Please check our Website Design Draft for more details.

Industry/Entity Type

Real estate Agency

Number of Pages Required

5+ page

Font styles to use
Sans Serif

Colors

Designer to choose colors to be used in the design.

```html
<!DOCTYPE html>
<html lang="en">
<head>
<meta charset="utf-8">
<title>Brindlewood Homes</title>
<link href="https://fonts.googleapis.com/css2?family=Poppins:ital,wght@0,300;0,400;0,500;0,600;1,400;1,500&family=Dancing+Script:wght@500&display=swap" rel="stylesheet">
<style>
:root{
  --gold:#e8b84a;
  --ink:#1c1c1f;
  --text:#333;
  --muted:#666;
  --grey:#efefef;
  --card:#e9e8e6;
  --night:#202127;
  --foot:#1a1a1c;
  --white:#fff;
}
*{box-sizing:border-box;margin:0;padding:0}
html,body{width:1200px;height:3839px;overflow:hidden}
body{position:relative;font-family:'Poppins',sans-serif;color:var(--text);background:var(--white)}
.abs{position:absolute}
.script{font-family:'Dancing Script',cursive;font-weight:500}
.gold{color:var(--gold)}
.btn{position:absolute;display:flex;align-items:center;justify-content:center;font-size:12px;font-weight:500;color:var(--ink);background:var(--gold)}
.btn.dark{background:#000;color:var(--gold)}
.section-title{position:absolute;left:0;width:1200px;text-align:center;font-size:28px;font-weight:400;color:var(--ink);letter-spacing:.3px}
.section-kicker{position:absolute;left:0;width:1200px;text-align:center;font-size:27px;color:var(--ink)}
.photo{position:absolute}

/* header */
.site-header{position:absolute;left:0;top:0;width:1200px;height:57px;background:var(--white)}
.brand{position:absolute;left:166px;top:10px;display:flex;align-items:center;gap:8px}
.brand-mark{width:26px;height:26px;background:var(--gold)}
.brand-name{font-size:24px;font-weight:600;color:var(--ink);line-height:1}
.top-phone{position:absolute;left:836px;top:3px;display:flex;align-items:center;gap:6px;font-size:15px;font-weight:600;color:var(--ink)}
.top-social{position:absolute;left:990px;top:6px;display:flex;gap:12px}
.top-social span{width:13px;height:13px;border-radius:50%;background:#3b7bd8}
.main-nav{position:absolute;left:593px;top:36px;display:flex;gap:22px;font-size:10px;font-weight:600;color:var(--ink)}

/* hero */
.hero{position:absolute;left:0;top:57px;width:1200px;height:423px;background:linear-gradient(160deg,#5b5e5a 0%,#8a8680 40%,#a98d74 60%,#4e5a52 100%)}
.hero h1{position:absolute;left:0;top:163px;width:1200px;text-align:center;font-size:35px;font-weight:600;color:var(--white);text-shadow:0 2px 6px rgba(0,0,0,.7)}

/* who */
.who-title{position:absolute;left:624px;top:563px;font-size:27px;color:var(--ink)}
.who-copy{position:absolute;left:624px;top:604px;width:390px;font-size:9.5px;line-height:15.5px;color:var(--text)}
.who-copy p+p{margin-top:10px}

/* stats */
.stats{position:absolute;left:0;top:876px;width:1200px;height:400px;background:var(--grey)}
.stat{position:absolute;top:185px;width:200px;text-align:center}
.diamond{position:relative;margin:0 auto;width:125px;height:125px}
.diamond::before{content:"";position:absolute;left:19px;top:19px;width:87px;height:87px;border:2px solid var(--ink);transform:rotate(45deg)}
.diamond span{position:absolute;left:0;top:0;width:125px;line-height:125px;font-size:28px;color:var(--ink)}
.stat-label{margin-top:6px;font-size:22px;color:var(--ink)}

/* tabs */
.tabs{position:absolute;left:365px;top:1372px;width:469px;height:25px;display:flex;border:1px solid var(--gold)}
.tabs span{flex:1;display:flex;align-items:center;justify-content:center;font-size:9px;color:var(--ink);border-right:1px solid var(--gold)}
.tabs span:last-child{border-right:0}
.tabs .active{background:var(--gold);position:relative}
.tabs .active::after{content:"";position:absolute;bottom:-6px;left:50%;margin-left:-5px;border:5px solid transparent;border-top-color:var(--gold);border-bottom:0}

/* team */
.member{position:absolute;top:1957px;width:232px;height:302px;background:var(--card)}
.member .avatar{position:absolute;left:41px;top:14px;width:150px;height:150px;border-radius:50%;border:2px solid var(--gold);background:linear-gradient(180deg,#d4d4d4,#8c8c8e)}
.member .name{position:absolute;top:171px;width:100%;text-align:center;font-size:14px;font-weight:600;color:var(--ink)}
.member .role{position:absolute;top:190px;width:100%;text-align:center;font-size:8.5px;line-height:11px;color:var(--text)}
.member ul{position:absolute;left:11px;top:236px;list-style:none;font-size:8.5px;color:var(--text)}
.member li{display:flex;align-items:center;gap:6px;height:19.5px}
.member svg{width:10px;height:10px}
.arrow{position:absolute;top:2086px}

/* testimonial */
.testimonials{position:absolute;left:0;top:2375px;width:1200px;height:561px;background:var(--night)}
.testimonials .script{position:absolute;top:22px;width:1200px;text-align:center;font-size:28px;color:var(--white)}
.testimonials h2{position:absolute;top:67px;width:1200px;text-align:center;font-size:28px;font-weight:400;color:var(--white)}
.client{position:absolute;left:518px;top:138px;width:164px;height:164px;border-radius:50%;border:5px solid #000;background:linear-gradient(180deg,#f0f0f0,#2e3a55)}
.client-name{position:absolute;top:330px;width:1200px;text-align:center;font-size:28px;font-style:italic;color:var(--gold)}
.quote{position:absolute;left:220px;top:386px;width:760px;text-align:center;font-size:16.5px;line-height:25px;font-style:italic;color:#e6e6e6}
.dots{position:absolute;top:482px;left:554px;display:flex;gap:6px}
.dots span{width:10px;height:10px;border-radius:50%;background:#cfcfcf}
.dots span:first-child{background:var(--gold)}

/* blog */
.post{position:absolute;top:3090px;width:385px;height:263px}
.post-info{position:absolute;left:0;top:0;width:235px;height:70px;background:rgba(255,255,255,.88);padding:10px 8px;font-size:10.5px;line-height:14px;color:var(--ink)}
.post-meta{display:flex;align-items:center;gap:6px;font-size:8.5px;margin-bottom:9px}
.post-meta b{font-weight:500;color:var(--gold)}
.post-go{position:absolute;left:235px;top:0;width:36px;height:36px;border:1px solid var(--gold);background:rgba(255,255,255,.5);display:flex;align-items:center;justify-content:center}

/* footer */
.site-footer{position:absolute;left:0;top:3498px;width:1200px;height:341px;background:var(--foot);color:var(--white)}
.site-footer h3{position:absolute;top:40px;font-size:21px;font-weight:400;padding-bottom:4px;border-bottom:1px solid var(--gold)}
.foot-about{position:absolute;left:177px;top:100px;width:238px;font-size:11px;line-height:18.7px;text-align:justify}
.foot-links{position:absolute;left:537px;top:98px;list-style:none;font-size:12px;line-height:22.6px}
.foot-news{position:absolute;left:766px;top:96px;width:250px;font-size:11px;line-height:18.5px}
.subscribe{position:absolute;left:765px;top:169px;width:257px;height:32px;border-radius:16px;background:var(--white);overflow:hidden}
.subscribe .field{position:absolute;left:60px;top:8px;font-size:11px;color:#999}
.subscribe .send{position:absolute;right:0;top:0;width:66px;height:32px;background:var(--gold);display:flex;align-items:center;justify-content:center}
.foot-social{position:absolute;left:811px;top:218px;display:flex;gap:15px}
.foot-social span{width:21px;height:21px;border-radius:50%;background:#2f6fd6}
.copyright{position:absolute;left:0;top:318px;width:1200px;text-align:center;font-size:8.5px;color:#ddd}
.copyright b{font-weight:400;color:var(--gold)}
</style>
</head>
<body>

<header class="site-header">
  <div class="brand"><span class="brand-mark"></span><span class="brand-name">Brindlewood</span></div>
  <div class="top-phone">
    <svg width="18" height="18" viewBox="0 0 24 24" fill="none" stroke="#1c1c1f" stroke-width="2"><circle cx="12" cy="12" r="10.5"/><path d="M8.5 7.5c0 4.5 3.5 8.5 8 9l1-2-2.5-1.2-1 1c-1.5-.7-2.7-2-3.4-3.5l1-1L10.5 7z" fill="#1c1c1f" stroke="none"/></svg>
    02 5550 1234
  </div>
  <div class="top-social"><span></span><span></span></div>
  <nav class="main-nav">
    <span>HOME</span><span>ABOUT US</span><span>LEASING</span><span>BUY</span><span>SELL</span><span>OUR TEAM</span><span>BLOG</span><span>CONTACT US</span>
  </nav>
</header>

<section class="hero" role="img" aria-label="Photo of a modern lounge with terracotta and teal armchairs, timber coffee tables and tall plants">
  <h1>Lorem ipsum dolor sit amet, consectetur</h1>
</section>
<div class="btn" style="left:433px;top:277px;width:155px;height:30px">Buy A Propertiy</div>
<div class="btn dark" style="left:621px;top:277px;width:154px;height:30px">Lease A Propertiy</div>

<!-- who we are -->
<div class="photo" role="img" aria-label="Photo of a glass-walled living room opening to a garden" style="left:195px;top:528px;width:152px;height:155px;background:linear-gradient(135deg,#3c3a36,#8e8a80 55%,#55624e)"></div>
<div class="photo" role="img" aria-label="Photo of a residential tower against blue sky" style="left:362px;top:593px;width:87px;height:89px;background:linear-gradient(180deg,#7ea6cf,#5d6a78 60%,#b08d6a)"></div>
<svg class="abs" style="left:435px;top:573px" width="34" height="48" viewBox="0 0 34 48"><path d="M10 10 22 0h12v26L22 48V14z" fill="#e8b84a"/></svg>
<div class="photo" role="img" aria-label="Photo of a white apartment tower" style="left:305px;top:698px;width:85px;height:87px;background:linear-gradient(180deg,#9cc0dd,#d9dde0 50%,#6c7a6a)"></div>
<svg class="abs" style="left:283px;top:753px" width="36" height="50" viewBox="0 0 36 50"><path d="M0 26 14 8v22h22L22 50H0z" fill="#e8b84a"/></svg>
<div class="photo" role="img" aria-label="Photo of a dining room with pendant lights" style="left:405px;top:698px;width:131px;height:130px;background:linear-gradient(160deg,#c9c3b8,#8f7a63 55%,#5a4a3c)"></div>

<h2 class="who-title"><span class="gold">WHO</span> WE ARE</h2>
<div class="who-copy">
  <p>Brindlewood Homes believes a home is more than a roof, and buying a property is one of the most important decisions people make. We are a real estate company located in Northvale, Canberra.</p>
  <p>Being a portfolio sales agent and property manager, coupled with our high-profile international real estate experience, Brindlewood is considered a market leader on the cutting edge with deep industry knowledge, ranging from landlord-tenant relationships, residential purchases.</p>
</div>
<div class="btn dark" style="left:742px;top:755px;width:155px;height:30px">Learn More</div>

<!-- statistics -->
<section class="stats">
  <div class="script" style="position:absolute;top:42px;width:1200px;text-align:center;font-size:26px;color:var(--ink)">Brindlewood</div>
  <div class="section-kicker" style="top:82px"><span class="gold">STA</span>TISTICS</div>
  <div class="stat" style="left:183px"><div class="diamond"><span>200</span></div><div class="stat-label script">Properties For Sale</div></div>
  <div class="stat" style="left:394px"><div class="diamond"><span>180</span></div><div class="stat-label script">Properties For Lease</div></div>
  <div class="stat" style="left:605px"><div class="diamond"><span>500</span></div><div class="stat-label script">Properties Sold</div></div>
  <div class="stat" style="left:816px"><div class="diamond"><span>400</span></div><div class="stat-label script">Properties Leased</div></div>
</section>

<!-- this month -->
<h2 class="section-title" style="top:1316px"><span class="gold">THIS MONTH</span> AT BRINDLEWOOD HOMES</h2>
<div class="tabs"><span class="active">FOR SALE</span><span>FOR LEASE</span><span>OPEN TIMES</span><span>SOLD</span><span>LEASED</span></div>

<div class="photo" role="img" aria-label="Photo of a two-storey modern house at dusk" style="left:191px;top:1532px;width:201px;height:203px;background:linear-gradient(180deg,#6f8aa6,#3b4550 55%,#4f6a3e)"></div>
<div class="photo" role="img" aria-label="Photo of a dining room with a glass wine wall" style="left:408px;top:1428px;width:260px;height:192px;background:linear-gradient(160deg,#d8d3cb,#9e9488 50%,#5c534a)"></div>
<div class="photo" role="img" aria-label="Photo of an open-plan office with city views" style="left:685px;top:1516px;width:104px;height:103px;background:linear-gradient(180deg,#aab5c0,#6b625a)"></div>
<div class="photo" role="img" aria-label="Photo of a rooftop terrace at sunset" style="left:806px;top:1590px;width:167px;height:154px;background:linear-gradient(180deg,#8ea7c4,#b7a898 50%,#3c3a38)"></div>
<div class="photo" role="img" aria-label="Photo of a rooftop pool deck" style="left:410px;top:1634px;width:114px;height:111px;background:linear-gradient(180deg,#c8d7e4,#6fb3c8 55%,#6e5d4d)"></div>
<div class="photo" role="img" aria-label="Photo of landscaped garden steps beside a building" style="left:539px;top:1636px;width:252px;height:199px;background:linear-gradient(160deg,#8a8a86,#5b5d52 45%,#3d5a2c)"></div>
<div class="btn" style="left:280px;top:1776px;width:154px;height:30px">View All</div>

<!-- team -->
<h2 class="section-title" style="top:1876px"><span class="gold">OUR</span> TEAM</h2>
<svg class="arrow" style="left:190px" width="14" height="38" viewBox="0 0 14 38"><path d="M12 1 2 19l10 18" fill="none" stroke="#e8b84a" stroke-width="2.5"/></svg>
<svg class="arrow" style="left:995px" width="14" height="38" viewBox="0 0 14 38"><path d="M2 1l10 18L2 37" fill="none" stroke="#e8b84a" stroke-width="2.5"/></svg>

<div class="member" style="left:221px">
  <div class="avatar" role="img" aria-label="Portrait photo of the principal"></div>
  <div class="name">Liam Chen</div>
  <div class="role">Principal</div>
  <ul>
    <li><svg viewBox="0 0 24 24" fill="none" stroke="#333" stroke-width="2"><circle cx="12" cy="12" r="10"/><path d="M8 7c0 5 4 9 9 9l.5-2-2.5-1-1 1c-1.5-.7-2.7-2-3.4-3.5l1-1L10 7z" fill="#333" stroke="none"/></svg>+61 5550 1234</li>
    <li><svg viewBox="0 0 24 24"><rect x="6" y="1" width="12" height="22" rx="2" fill="none" stroke="#333" stroke-width="2.4"/></svg>0400 555 019</li>
    <li><svg viewBox="0 0 24 24"><path d="M1 5h22v14H1z" fill="#333"/><path d="M1 5l11 8 11-8" fill="none" stroke="#e9e8e6" stroke-width="2"/></svg>liam@brindlewoodhomes.com.au</li>
  </ul>
</div>
<div class="member" style="left:483px">
  <div class="avatar" role="img" aria-label="Portrait photo of the business relationship manager"></div>
  <div class="name">Mara Lin</div>
  <div class="role">Business Relationship Manager &amp;<br>Senior Property Manager</div>
  <ul>
    <li><svg viewBox="0 0 24 24" fill="none" stroke="#333" stroke-width="2"><circle cx="12" cy="12" r="10"/><path d="M8 7c0 5 4 9 9 9l.5-2-2.5-1-1 1c-1.5-.7-2.7-2-3.4-3.5l1-1L10 7z" fill="#333" stroke="none"/></svg>+61 5550 1234</li>
    <li><svg viewBox="0 0 24 24"><rect x="6" y="1" width="12" height="22" rx="2" fill="none" stroke="#333" stroke-width="2.4"/></svg>0400 555 027</li>
    <li><svg viewBox="0 0 24 24"><path d="M1 5h22v14H1z" fill="#333"/><path d="M1 5l11 8 11-8" fill="none" stroke="#e9e8e6" stroke-width="2"/></svg>mara.lin@brindlewoodhomes.com.au</li>
  </ul>
</div>
<div class="member" style="left:745px">
  <div class="avatar" role="img" aria-label="Portrait photo of the property manager"></div>
  <div class="name">Tessa Wong</div>
  <div class="role">Property Manager</div>
  <ul>
    <li><svg viewBox="0 0 24 24" fill="none" stroke="#333" stroke-width="2"><circle cx="12" cy="12" r="10"/><path d="M8 7c0 5 4 9 9 9l.5-2-2.5-1-1 1c-1.5-.7-2.7-2-3.4-3.5l1-1L10 7z" fill="#333" stroke="none"/></svg>+61 5550 1234</li>
    <li><svg viewBox="0 0 24 24"><rect x="6" y="1" width="12" height="22" rx="2" fill="none" stroke="#333" stroke-width="2.4"/></svg>0400 555 019</li>
    <li><svg viewBox="0 0 24 24"><path d="M1 5h22v14H1z" fill="#333"/><path d="M1 5l11 8 11-8" fill="none" stroke="#e9e8e6" stroke-width="2"/></svg>inspect@brindlewoodhomes.com.au</li>
  </ul>
</div>
<div class="btn" style="left:523px;top:2295px;width:155px;height:30px">View All</div>

<!-- testimonials -->
<section class="testimonials">
  <div class="script">Testimonials</div>
  <h2><span class="gold">PEOPLE</span> TALK ABOUT US</h2>
  <div class="client" role="img" aria-label="Portrait photo of a client"></div>
  <div class="client-name">Nina HALE</div>
  <p class="quote">Very good service. Our property manager is very responsible, prompting and cares about detail. They use the system to track everything so no need to worry about miscommunication. I strongly recommend this agent.</p>
  <div class="dots"><span></span><span></span><span></span><span></span><span></span><span></span></div>
</section>

<!-- blog -->
<div class="script" style="position:absolute;top:2975px;width:1200px;text-align:center;font-size:28px;color:var(--ink)">Blog</div>
<h2 class="section-title" style="top:3021px"><span class="gold">LATEST</span> NEWS</h2>

<article class="post" style="left:178px" role="img" aria-label="Photo of a mid-rise apartment building above a street">
  <div style="position:absolute;inset:0;background:linear-gradient(180deg,#c9c4ba,#a58d6e 50%,#4f4a40)"></div>
  <div class="post-info">
    <div class="post-meta"><svg width="11" height="11" viewBox="0 0 24 24" fill="none" stroke="#333" stroke-width="2"><circle cx="12" cy="12" r="10"/><path d="M12 6v6l4 2"/></svg>May 21, 2022 &nbsp;&nbsp;|&nbsp;&nbsp; by <b>Admin</b></div>
    Lorem ipsum dolor sit amet, con sec tetur adipis eiusmo...
  </div>
  <div class="post-go"><svg width="20" height="14" viewBox="0 0 20 14" fill="none" stroke="#e8b84a" stroke-width="1.6"><path d="M0 7h18M12 1l6 6-6 6"/></svg></div>
</article>
<article class="post" style="left:637px" role="img" aria-label="Aerial photo of city apartment towers">
  <div style="position:absolute;inset:0;background:linear-gradient(160deg,#b9c2c8,#8b8f8c 50%,#5c625c)"></div>
  <div class="post-info">
    <div class="post-meta"><svg width="11" height="11" viewBox="0 0 24 24" fill="none" stroke="#333" stroke-width="2"><circle cx="12" cy="12" r="10"/><path d="M12 6v6l4 2"/></svg>May 22, 2022 &nbsp;&nbsp;|&nbsp;&nbsp; by <b>Admin</b></div>
    Lorem ipsum dolor sit amet, con sect etur adipis eiusmo...
  </div>
  <div class="post-go"><svg width="20" height="14" viewBox="0 0 20 14" fill="none" stroke="#e8b84a" stroke-width="1.6"><path d="M0 7h18M12 1l6 6-6 6"/></svg></div>
</article>
<div class="btn" style="left:523px;top:3387px;width:155px;height:30px">View All Blog</div>

<!-- footer -->
<footer class="site-footer">
  <h3 style="left:180px">About Us</h3>
  <p class="foot-about">Helping landlords and vendor alike to complete efficient property transactions is our signature talent. Our poise, precision, and insight give us an unparalleled advantage. Beyond the core real estate services, we engender trust and cultivate relationships, an approach that generates repeat business from a high-quality client base.</p>
  <h3 style="left:535px">Quick Links</h3>
  <ul class="foot-links"><li>Home</li><li>About us</li><li>Leasing</li><li>Buy</li><li>Sell</li><li>Our Team</li><li>Blog</li><li>Contact Us</li></ul>
  <h3 style="left:767px">Our News Letter</h3>
  <p class="foot-news">Lorem ipsum dolor sit amet, consectetur adipiscing elit, sed do eiusmod tempor incididunt ut labore et dolore.....</p>
  <div class="subscribe">
    <svg class="abs" style="left:18px;top:10px" width="20" height="13" viewBox="0 0 20 13"><path d="M0 0h20v13H0z" fill="#888"/><path d="M0 0l10 7 10-7" fill="none" stroke="#fff" stroke-width="1.5"/></svg>
    <span class="field">Emailaddress</span>
    <div class="send"><svg width="22" height="20" viewBox="0 0 22 20"><path d="M0 8 22 0 16 20 10 13 18 4 8 11z" fill="#1a1a1c"/></svg></div>
  </div>
  <div class="foot-social"><span></span><span></span><span></span><span></span></div>
  <div class="copyright">Copyright © 2022 Brindlewood Homes. Use of this website constitutes acceptance of our <b>User Agreement</b> and <b>Privacy Policy</b>.</div>
</footer>

</body>
</html>
```